Varnek Group Business Card

Varnek Group — Business Card Design Brief
Overview
Design a double-sided business card for Varnek Group that highlights our two service arms: Varnek Communications (telecommunications) and Varnek Energy (business energy solutions). The card should feel smart and stand out when handed to clients.

Objectives
Showcase our areas of specialty clearly.
Reflect the overall Varnek / Varnek Group brand while acknowledging both arms.
Explore using both logos (Communications + Energy) or one unified logo, depending on the design.

Deliverables
One double-sided business card design (front + back).

Content & Copy
Front (preferred): Logo: Varnek / Varnek Group
Descriptor: Business Communications | Business Energy
Back:My contact details and company details
Core products: Business Mobile • Telephony • Internet • Business Energy Solutions

Brand & Visual Direction
We have a group logo currently tailored more toward telecoms, plus a separate Varnek Energy logo.
Please explore layouts that use both logos or just one, whichever works best.
Color: I wouldn't mind seeing an option using our the Blue/Purple gradient from our website (varnek-example.co.uk), but also open to non-gradient approaches and other colours..

Overall look: Smart, modern, and distinctive.
Format & Print Specs
Double-sided business card format. (Use a standard size

Must-Haves
Front: Varnek wording or Varnek Group wording with atleast 1 logo also on front “Business Communications | Business Energy.”

Back: Contact + company details and core products.
A design that stands out while remaining professional.

Nice-to-Have Options
A gradient version using our site’s Blue/Purple gradient.
A non-gradient version.
A dual-logo treatment versus a single-logo treatment.

Thanks
Dominic

```html
<!DOCTYPE html>
<html lang="en">
<head>
<meta charset="utf-8">
<title>Varnek Group Business Card</title>
<link rel="stylesheet" href="https://fonts.googleapis.com/css2?family=Poppins:wght@400;500;600;700;800&display=swap">
<style>
  :root {
    --backdrop: #e4e4e4;
    --card: #fbf9f3;
    --navy: #26236b;
    --blue: #1f8fe0;
    --green: #6bbf3a;
    --text: #2b2b3a;
    --muted: #555566;
    --accent: #8a3fb8;
    --band-text: #ffffff;
  }
  * { box-sizing: border-box; margin: 0; padding: 0; }
  html, body { width: 900px; height: 1200px; overflow: hidden; }
  body {
    background: var(--backdrop);
    font-family: "Poppins", Arial, sans-serif;
    color: var(--text);
    position: relative;
  }
  .card {
    position: absolute;
    left: 144px;
    width: 612px;
    height: 345px;
    background: var(--card);
    box-shadow: 0 10px 28px rgba(0,0,0,0.18);
    overflow: hidden;
  }
  .card--front { top: 200px; }
  .card--back { top: 650px; }

  /* Front */
  .front-brand {
    position: absolute;
    inset: 0;
    display: flex;
    flex-direction: column;
    align-items: center;
    justify-content: center;
    gap: 14px;
  }
  .brand-dot {
    width: 74px; height: 74px;
    border-radius: 50%;
    background: var(--blue);
  }
  .front-name {
    font-weight: 800;
    color: var(--navy);
    text-align: center;
    line-height: 1.05;
  }
  .front-name .line-main { display: block; font-size: 56px; letter-spacing: 1px; }
  .front-name .line-sub { display: block; font-size: 19px; letter-spacing: 2px; }

  /* Back */
  .back-brand {
    position: absolute;
    left: 30px; top: 48px;
    width: 220px;
    display: flex;
    flex-direction: column;
    align-items: center;
    gap: 12px;
  }
  .back-brand .brand-dot { width: 92px; height: 92px; background: var(--green); }
  .back-name {
    font-weight: 800;
    font-size: 52px;
    color: var(--navy);
    letter-spacing: 1px;
    line-height: 1;
  }
  .divider {
    position: absolute;
    left: 268px; top: 40px;
    width: 3px; height: 210px;
    background: var(--navy);
  }
  .contact {
    position: absolute;
    left: 288px; top: 40px;
    width: 300px;
  }
  .person-name { font-size: 25px; font-weight: 700; color: var(--navy); line-height: 1.1; }
  .person-role { font-size: 13px; color: var(--muted); margin-bottom: 14px; }
  .contact-list { list-style: none; }
  .contact-list li {
    display: flex; align-items: center; gap: 8px;
    font-size: 13px; line-height: 1.75;
  }
  .contact-list svg { width: 13px; height: 13px; flex: none; }
  .address { font-size: 13px; line-height: 1.5; margin-top: 14px; }
  .products-band {
    position: absolute;
    left: 0; right: 0; bottom: 24px;
    height: 38px;
    background: var(--navy);
    color: var(--band-text);
    font-size: 15px;
    font-weight: 500;
    display: flex; align-items: center;
    padding-left: 24px;
    letter-spacing: 0.2px;
  }
</style>
</head>
<body>
  <section class="card card--front" aria-label="Business card front">
    <div class="front-brand">
      <span class="brand-dot" aria-hidden="true"></span>
      <h1 class="front-name">
        <span class="line-main">VARNEK</span>
        <span class="line-sub">COMMUNICATIONS</span>
      </h1>
    </div>
  </section>

  <section class="card card--back" aria-label="Business card back">
    <div class="back-brand">
      <span class="brand-dot" aria-hidden="true"></span>
      <span class="back-name">VARNEK</span>
    </div>
    <div class="divider" aria-hidden="true"></div>
    <div class="contact">
      <p class="person-name">Elias Brandt</p>
      <p class="person-role">Geschäftsführer</p>
      <ul class="contact-list">
        <li>
          <svg viewBox="0 0 24 24" aria-hidden="true"><path fill="var(--accent)" d="M6.6 10.8a15.1 15.1 0 0 0 6.6 6.6l2.2-2.2a1 1 0 0 1 1-.25 11.4 11.4 0 0 0 3.6.57 1 1 0 0 1 1 1V20a1 1 0 0 1-1 1A17 17 0 0 1 3 4a1 1 0 0 1 1-1h3.5a1 1 0 0 1 1 1c0 1.25.2 2.45.57 3.57a1 1 0 0 1-.25 1z"/></svg>
          +44 0161 555 0142
        </li>
        <li>
          <svg viewBox="0 0 24 24" aria-hidden="true"><rect x="2" y="5" width="20" height="14" rx="2" fill="var(--accent)"/><path d="M3 6l9 7 9-7" fill="none" stroke="#fff" stroke-width="2"/></svg>
          info@varnek-example.co.uk
        </li>
        <li>
          <svg viewBox="0 0 24 24" aria-hidden="true"><circle cx="12" cy="12" r="10" fill="var(--accent)"/><path d="M2 12h20M12 2c3 3 3 17 0 20M12 2c-3 3-3 17 0 20" fill="none" stroke="#fff" stroke-width="1.5"/></svg>
          varnek-example.co.uk
        </li>
      </ul>
      <p class="address">24 Harbour Row, Manchester,<br>England, M1 7QZ</p>
    </div>
    <div class="products-band">Business Mobile • Telephony • Internet • Business Energy Solutions</div>
  </section>
</body>
</html>
```